I need a letterhead for my new business called "Bramblecrest Personal Training." My business is online and I customize training/meal plans for clients. My specialties are powerlifting, olympic weightlifting and strongman training. I would like to see a design that uses an oldtime strongman holding a barbell overhead in his right hand and a kettle bell hanging in his left hand. This needs to look masculine and not too cartoony. The final design should communicate power, strength and determination.

```html
<!DOCTYPE html>
<html lang="en">
<head>
<meta charset="utf-8">
<title>Bramblecrest Personal Training – Letterhead</title>
<link rel="stylesheet" href="https://fonts.googleapis.com/css2?family=Lobster+Two:ital,wght@1,700&family=Open+Sans:wght@400&family=Roboto+Condensed:wght@400&display=swap">
<style>
  :root {
    --brand-red: #b2231f;
    --ink: #333333;
    --paper: #ffffff;
    --edge: #c8c8c8;
    --wave-blue: #0091d9;
    --wave-green: #84c225;
    --wave-lightgreen: #b9d98a;
    --wave-red: #d8261d;
    --figure-dark: #2a2a2a;
    --figure-mid: #8a8a8a;
  }
  html, body {
    margin: 0;
    padding: 0;
    width: 930px;
    height: 1200px;
    overflow: hidden;
    background: var(--paper);
  }
  .letterhead {
    position: relative;
    width: 930px;
    height: 1200px;
    box-sizing: border-box;
    border: 1px solid var(--edge);
    background: var(--paper);
    overflow: hidden;
  }
  .brand {
    position: absolute;
    top: 44px;
    left: 0;
    width: 100%;
    text-align: center;
  }
  .brand-name {
    margin: 0;
    font-family: "Lobster Two", cursive;
    font-style: italic;
    font-weight: 700;
    font-size: 46px;
    line-height: 1;
    color: var(--brand-red);
  }
  .specialties {
    margin: 14px 0 0;
    font-family: "Open Sans", sans-serif;
    font-size: 17px;
    color: var(--ink);
    letter-spacing: 0.2px;
  }
  .specialties .bullet {
    display: inline-block;
    width: 9px;
    height: 9px;
    margin: 0 9px 2px;
    background: var(--brand-red);
    vertical-align: middle;
  }
  .waves {
    position: absolute;
    left: 0;
    top: 0;
    width: 930px;
    height: 1200px;
  }
  .strongman-figure {
    position: absolute;
    left: 722px;
    top: 915px;
    width: 175px;
    height: 215px;
    background: linear-gradient(180deg, var(--figure-mid), var(--figure-dark));
    opacity: 0.85;
  }
  .contact {
    position: absolute;
    left: 57px;
    top: 1133px;
    margin: 0;
    font-family: "Roboto Condensed", sans-serif;
    font-size: 12.5px;
    line-height: 18px;
    color: var(--paper);
  }
  .contact p { margin: 0; }
</style>
</head>
<body>
<div class="letterhead">
  <header class="brand">
    <h1 class="brand-name">Bramblecrest Personal Training</h1>
    <p class="specialties">Powerlifting<span class="bullet"></span>Olympic Weightlifting<span class="bullet"></span>Strongman Training</p>
  </header>

  <svg class="waves" viewBox="0 0 930 1200" aria-hidden="true">
    <path d="M0,795 C80,960 250,1095 510,1098 L0,1160 Z" fill="var(--wave-blue)"/>
    <path d="M0,985 C110,1080 270,1120 470,1102 C600,1080 720,1068 800,1098 C850,1120 900,1150 930,1175 L930,1200 L0,1200 Z" fill="var(--wave-green)"/>
    <path d="M0,985 C110,1080 270,1120 470,1102" fill="none" stroke="var(--paper)" stroke-width="3"/>
    <path d="M590,1200 C700,1150 840,1118 930,1160 L930,1200 Z" fill="var(--wave-lightgreen)" stroke="var(--paper)" stroke-width="2"/>
    <path d="M640,1200 C740,1168 860,1155 930,1190 L930,1200 Z" fill="var(--wave-red)" stroke="var(--paper)" stroke-width="2"/>
  </svg>

  <div class="strongman-figure" role="img" aria-label="Illustration of an old-time strongman holding a barbell overhead in one hand and a kettlebell in the other"></div>

  <address class="contact">
    <p>Head Office: 48-B, Alder Crest Lane, Fairmont-481207 &nbsp;|&nbsp; Reg. Office: 315-C-Oakridge House, Mill Road, Fairmont</p>
    <p>Phone: (014) 586 20 &nbsp;|&nbsp; Mobile : 91 6305184927 &nbsp;|&nbsp; E-mail: bramblecrest@mailbox.com &nbsp;|&nbsp; Web: www.bramblecrestpt.com</p>
  </address>
</div>
</body>
</html>
```